Business card, folder, and other items for LMV
Lakemoor Vale Oncology, PLLC business cards and material
Please show us folder designs that will house these documents as well.
Thanks for all the great designs.
After seeing double sided designs above, we would like to utilize this design feature. Please submit double sided designs. Thank you.
Please show designs of folder and stationery as well. Current designs look very nice. Thanks for the submissions.

```html
<!DOCTYPE html>
<html lang="en">
<head>
<meta charset="utf-8">
<title>Lakemoor Vale Oncology, PLLC – Business Card</title>
<link rel="stylesheet" href="https://fonts.googleapis.com/css2?family=Arimo:wght@400;700&display=swap">
<style>
  :root {
    --page-bg: #ecebe8;
    --card-bg: #ffffff;
    --brand-blue: #2d63b8;
    --brand-blue-dark: #173f8a;
    --brand-blue-light: #5b8ad6;
    --rule-grey: #c9ccd2;
    --text-dark: #2b2b2b;
    --text-grey: #7a7a7a;
  }
  * { margin: 0; padding: 0; box-sizing: border-box; }
  html, body {
    width: 1200px; height: 778px; overflow: hidden;
    background: var(--page-bg);
    font-family: "Arimo", Arial, sans-serif;
  }
  .business-card {
    position: absolute; left: 50px; top: 109px;
    width: 1100px; height: 560px;
    background: linear-gradient(180deg, var(--card-bg) 80%, #f1f2f4 100%);
    border-radius: 34px;
    overflow: hidden;
    box-shadow: 0 6px 18px rgba(0,0,0,0.18);
  }
  .side-band {
    position: absolute; left: 0; top: 0; bottom: 0; width: 64px;
    background: linear-gradient(90deg, var(--brand-blue-dark), var(--brand-blue) 55%, var(--brand-blue-light));
  }
  .side-rule {
    position: absolute; left: 76px; top: 0; bottom: 0; width: 10px;
    background: var(--rule-grey);
  }
  .brand-mark {
    position: absolute; left: 128px; top: 58px;
    display: flex; align-items: center; gap: 18px;
  }
  .brand-dot {
    width: 96px; height: 96px; border-radius: 50%;
    background: var(--brand-blue);
  }
  .brand-name {
    font-size: 104px; font-weight: 700; line-height: 1;
    color: var(--brand-blue); letter-spacing: 1px;
  }
  .person {
    position: absolute; right: 56px; top: 208px; text-align: right;
  }
  .person-name {
    font-size: 36px; font-weight: 400; color: var(--brand-blue);
  }
  .person-title {
    margin-top: 6px; font-size: 25px; font-weight: 700; color: var(--text-grey);
  }
  .mailing-address {
    position: absolute; left: 146px; top: 300px;
    font-size: 24px; line-height: 34px; color: var(--text-dark);
    font-style: normal;
  }
  .contact-list {
    position: absolute; left: 146px; top: 448px; list-style: none;
    font-size: 24px; line-height: 36px; color: var(--text-dark);
  }
  .contact-list li { display: flex; align-items: center; gap: 12px; }
  .contact-icon { width: 18px; height: 18px; flex: none; }
</style>
</head>
<body>
  <div class="business-card">
    <div class="side-band"></div>
    <div class="side-rule"></div>

    <div class="brand-mark" aria-label="Lakemoor Vale Oncology, PLLC">
      <div class="brand-dot"></div>
      <span class="brand-name">LMV</span>
    </div>

    <div class="person">
      <div class="person-name">Mara Kherwin, M.D., DABR</div>
      <div class="person-title">President</div>
    </div>

    <address class="mailing-address">
      P.O. Box 2481<br>
      Brookfield, KY 40219-2481
    </address>

    <ul class="contact-list">
      <li>
        <svg class="contact-icon" viewBox="0 0 20 20" aria-hidden="true">
          <path d="M5 2c1 0 2 3 2 4s-2 1-1 3 3 4 5 5 2-1 3-1 4 1 4 2-2 3-3 3C8 18 2 12 2 5c0-1 2-3 3-3z" fill="var(--brand-blue)"/>
        </svg>
        1-555-014-2287
      </li>
      <li>
        <svg class="contact-icon" viewBox="0 0 20 20" aria-hidden="true">
          <rect x="1.5" y="4" width="17" height="12" fill="none" stroke="var(--brand-blue)" stroke-width="2"/>
          <path d="M2 5l8 6 8-6" fill="none" stroke="var(--brand-blue)" stroke-width="2"/>
        </svg>
        mkherwin@lakemoorvaleonc.com
      </li>
      <li>
        <svg class="contact-icon" viewBox="0 0 20 20" aria-hidden="true">
          <circle cx="10" cy="10" r="8.5" fill="var(--brand-blue)"/>
          <path d="M1.5 10h17M10 1.5c-4 4-4 13 0 17M10 1.5c4 4 4 13 0 17" fill="none" stroke="#fff" stroke-width="1.3"/>
        </svg>
        www.lakemoorvaleonc.com
      </li>
    </ul>
  </div>
</body>
</html>
```